Modern Quillby Tree Care Website

I need a website for a full service Tree Care company. The company provides tree pruning, tree removal, tree preservation, emergency services, stump grinding, and emergency tree services.

Target Market(s)

Customers that need tree services

Industry/Entity Type

Landscaping, Tree Services

Coding

Coded - Design and coding required

Number of Pages Required

5+ page

Font styles to use
Sans Serif

Requirements
Must have
• Good clean design that showcases the services the company provides.
Nice to have
• Services page; contact form, blog, home page, about page

```html
<!DOCTYPE html>
<html lang="en">
<head>
<meta charset="UTF-8">
<title>Quillby Tree Care</title>
<link rel="stylesheet" href="https://fonts.googleapis.com/css2?family=Ubuntu:wght@500;700&family=Open+Sans:wght@400;600;700&display=swap">
<style>
:root{
  --navy:#1b3c80;
  --ink:#0b1428;
  --green:#8cc63f;
  --green-dark:#76b12e;
  --light:#f3f4f3;
  --text:#555b66;
  --white:#ffffff;
}
*{margin:0;padding:0;box-sizing:border-box}
html,body{width:1200px;height:4371px;overflow:hidden}
body{position:relative;background:var(--white);font-family:"Open Sans",sans-serif;color:var(--text)}
.abs{position:absolute}
h1,h2,h3,.heading{font-family:"Ubuntu",sans-serif;font-weight:700}
.btn{position:absolute;display:flex;align-items:center;justify-content:center;background:var(--green);color:var(--white);font-family:"Open Sans",sans-serif;font-weight:700;font-size:13px;letter-spacing:.3px}
.label{position:absolute;color:var(--green);font-family:"Ubuntu",sans-serif;font-weight:500;font-size:16px}
.section-title{position:absolute;color:var(--navy);font-size:46px;line-height:56px}

/* header */
.topbar{position:absolute;left:390px;top:0;width:810px;height:31px;background:var(--navy);clip-path:polygon(28px 0,100% 0,100% 100%,0 100%)}
.topbar .appoint{position:absolute;left:202px;top:0;width:234px;height:31px;background:var(--green)}
.topbar span{position:absolute;top:8px;color:var(--white);font-size:11px;font-weight:600;display:flex;align-items:center;gap:8px}
.brand{position:absolute;left:107px;top:26px;display:flex;align-items:center;gap:10px}
.brand .mark{width:46px;height:46px;background:var(--green)}
.brand .name{font-family:"Ubuntu",sans-serif;font-weight:700;font-size:24px;color:var(--navy);line-height:26px;width:150px}
.nav a{position:absolute;top:60px;font-size:11.5px;font-weight:600;color:#333a45;text-decoration:none}
.contact-btn{position:absolute;left:930px;top:52px;width:119px;height:30px;border:2px solid var(--green);border-radius:4px;color:var(--green);font-size:11px;display:flex;align-items:center;justify-content:center}

/* hero */
.hero{position:absolute;left:0;top:98px;width:1200px;height:734px}
.hero-photo{position:absolute;inset:0;background:radial-gradient(ellipse at 70% 40%,#5c6a3c 0%,#39442a 45%,#24291d 100%)}
.hero .welcome{position:absolute;left:110px;top:164px;color:var(--white);font-size:13px;display:flex;align-items:center;gap:10px}
.hero .welcome i{display:block;width:44px;height:2px;background:var(--white)}
.hero h1{position:absolute;left:110px;top:192px;color:var(--white);font-size:41px;line-height:57px}
.hero p{position:absolute;left:110px;top:318px;width:410px;color:#e8ecdf;font-size:13px;line-height:21px}
.hero .btn{left:110px;top:434px;width:193px;height:41px}

/* about */
.about-copy{position:absolute;left:636px;top:922px;width:470px}
.about-copy p{font-size:13.5px;line-height:24.5px;margin-bottom:16px}

/* services */
.services{position:absolute;left:0;top:1443px;width:1200px;height:647px;background:var(--ink)}
.services .eyebrow{position:absolute;width:100%;top:96px;text-align:center;color:var(--white);font-size:16px;font-weight:600}
.services h2{position:absolute;width:100%;top:128px;text-align:center;color:var(--white);font-size:46px}
.service{position:absolute;top:290px;width:319px;height:290px}
.service .photo{position:absolute;left:0;top:0;width:319px;height:242px}
.service .badge{position:absolute;left:121px;top:-55px;width:78px;height:78px;border-radius:50%;border:1px solid rgba(255,255,255,.25);display:flex;align-items:center;justify-content:center}
.service .badge b{width:64px;height:64px;border-radius:50%;background:var(--green);display:flex;align-items:center;justify-content:center}
.service .caption{position:absolute;left:17px;top:208px;width:285px;height:79px;background:var(--white);border-radius:4px;text-align:center;padding-top:16px}
.service h3{font-size:18px;color:var(--navy)}
.service .more{font-size:13.5px;color:var(--text);margin-top:4px;display:flex;justify-content:center;align-items:center;gap:6px;font-weight:600}

/* why */
.why{position:absolute;left:0;top:2090px;width:1200px;height:622px;background:var(--light)}
.tab{position:absolute;top:261px;height:44px;border-radius:4px;font-family:"Ubuntu",sans-serif;font-weight:500;font-size:16px;display:flex;align-items:center;justify-content:center;background:var(--white);color:var(--green)}
.tab.active{background:var(--green);color:var(--white)}
.why .intro{position:absolute;left:368px;top:348px;width:300px;font-size:13.5px;line-height:24px}
.check{position:absolute;left:368px;font-size:13.5px;display:flex;align-items:center;gap:10px}

/* cta */
.cta{position:absolute;left:0;top:2712px;width:1200px;height:436px;background:radial-gradient(ellipse at 40% 50%,#3b3a28 0%,#2a2a1c 55%,#1d1e15 100%)}
.cta h2{position:absolute;left:109px;top:105px;color:var(--white);font-size:44px;line-height:56px}
.cta .btn{left:109px;top:292px;width:147px;height:41px;border-radius:3px}
.pill{position:absolute;left:691px;width:392px;height:46px;border-radius:8px;background:rgba(255,255,255,.18);border:1px solid rgba(255,255,255,.12);color:var(--white);font-size:12px;font-weight:700;display:flex;align-items:center;padding-left:52px}

/* testimonials */
.reviews{position:absolute;left:0;top:3148px;width:1200px;height:900px;background:var(--light)}
.reviews h2{position:absolute;width:100%;top:120px;text-align:center;color:var(--navy);font-size:46px}
.review{position:absolute;top:226px;width:320px;height:270px}
.review .avatar{position:absolute;left:0;top:0;width:87px;height:122px;border-radius:6px}
.review .who{position:absolute;left:107px;top:24px}
.review .who strong{display:block;font-family:"Ubuntu",sans-serif;font-weight:500;font-size:17px;color:#3d4350}
.review .who small{display:block;font-size:11.5px;margin-top:6px}
.review .card{position:absolute;left:19px;top:105px;width:302px;height:161px;background:var(--white);box-shadow:0 6px 20px rgba(0,0,0,.05);padding:36px 20px 0 31px;font-size:13.5px;line-height:24px}
.review .quote{position:absolute;left:260px;top:86px;color:var(--green);font-family:"Ubuntu",sans-serif;font-weight:700;font-size:62px;line-height:40px}

/* footer */
.footer{position:absolute;left:0;top:3852px;width:1200px;height:519px}
.footer .col-title{position:absolute;color:var(--white);font-family:"Ubuntu",sans-serif;font-weight:500;font-size:19px}
.footer p{position:absolute;color:var(--white)}
.social{position:absolute;top:4236px;width:33px;height:31px;border-radius:3px;background:rgba(255,255,255,.18)}
</style>
</head>
<body>

<!-- header -->
<div class="topbar">
  <div class="appoint"></div>
  <span style="left:54px">
    <svg width="14" height="14" viewBox="0 0 24 24" fill="none" stroke="#fff" stroke-width="2"><path d="M22 16.9v3a2 2 0 0 1-2.2 2 19.8 19.8 0 0 1-8.6-3.1 19.5 19.5 0 0 1-6-6A19.8 19.8 0 0 1 2.1 4.2 2 2 0 0 1 4.1 2h3a2 2 0 0 1 2 1.7c.1 1 .4 1.9.7 2.8a2 2 0 0 1-.5 2.1L8 9.9a16 16 0 0 0 6 6l1.3-1.3a2 2 0 0 1 2.1-.4c.9.3 1.8.6 2.8.7a2 2 0 0 1 1.7 2z"/></svg>
    555 - 210 - 4830</span>
  <span style="left:236px">
    <svg width="14" height="14" viewBox="0 0 24 24" fill="none" stroke="#fff" stroke-width="2"><rect x="3" y="4" width="18" height="18" rx="2"/><path d="M16 2v4M8 2v4M3 10h18"/></svg>
    REQUEST AN APPOINTMENT</span>
  <span style="left:468px">
    <svg width="13" height="13" viewBox="0 0 24 24" fill="none" stroke="#fff" stroke-width="2"><path d="M12 22s7-6.5 7-12a7 7 0 0 0-14 0c0 5.5 7 12 7 12z"/><circle cx="12" cy="10" r="2.5"/></svg>
    88 Maple Hollow Road</span>
</div>

<div class="brand"><div class="mark"></div><div class="name">Quillby Tree Care</div></div>

<nav class="nav">
  <a style="left:395px">Home</a>
  <a style="left:470px">About Us</a>
  <a style="left:545px">Services</a>
  <a style="left:633px">Gallery</a>
  <a style="left:726px">Our Team</a>
</nav>
<div class="contact-btn">CONTACT US</div>

<!-- hero -->
<section class="hero">
  <div class="hero-photo" role="img" aria-label="Arborist in safety gear cutting a large tree trunk in a forest"></div>
  <div class="welcome">Welcome <i></i></div>
  <h1>Your Partner in<br>Tree Presevation</h1>
  <p>Lorem ipsum dolor sit amet, consectetur adipiscing elit, sed do eiusmod tempor incididunt ut labore et dolore magna Lorem ipsum dolor sit amet, consectetur adipiscing elit, sed do eiusmod tempor incididunt ut labore et dolore magna</p>
  <div class="btn">Discover more</div>
  <svg class="abs" style="left:0;top:0" width="1200" height="734" viewBox="0 98 1200 734">
    <path d="M0 640 C 250 790 420 835 600 835 C 820 835 1050 770 1200 640 L1200 832 L0 832 Z" fill="#fff"/>
  </svg>
</section>

<!-- about -->
<svg class="abs" style="left:98px;top:888px" width="467" height="465" viewBox="0 0 467 465" role="img" aria-label="Collage of four photos showing tree workers cutting, climbing and clearing trees">
  <defs>
    <linearGradient id="g1" x1="0" y1="0" x2="1" y2="1"><stop offset="0" stop-color="#6f8a3a"/><stop offset="1" stop-color="#3b4a26"/></linearGradient>
    <linearGradient id="g2" x1="0" y1="0" x2="1" y2="1"><stop offset="0" stop-color="#5a7a9a"/><stop offset="1" stop-color="#2c3e5c"/></linearGradient>
    <linearGradient id="g3" x1="0" y1="0" x2="1" y2="1"><stop offset="0" stop-color="#8a6a4a"/><stop offset="1" stop-color="#4a3a28"/></linearGradient>
    <linearGradient id="g4" x1="0" y1="0" x2="1" y2="1"><stop offset="0" stop-color="#4c6a3a"/><stop offset="1" stop-color="#2a3a22"/></linearGradient>
  </defs>
  <polygon points="233,0 345,112 233,224 121,112" fill="url(#g1)"/>
  <polygon points="355,122 467,234 355,346 243,234" fill="url(#g2)"/>
  <polygon points="111,122 223,234 111,346 -1,234" fill="url(#g3)"/>
  <polygon points="233,244 345,356 233,465 121,356" fill="url(#g4)"/>
  <circle cx="233" cy="234" r="44" fill="#fff"/>
</svg>

<div class="label" style="left:636px;top:921px">Who We Are</div>
<h2 class="section-title" style="left:636px;top:952px">We Offer Sustainable<br>Tree Solutions</h2>
<div class="about-copy" style="top:1069px">
  <p>Lorem ipsum dolor sit amet, consectetur adipiscing elit, sed do eiusmod tempor incididunt ut labore et dolore magna aliqua.Lorem ipsum dolor sit amet. Lorem ipsum dolor sit amet, consectetur adip iscing elit, sed do eiusmod tempor incididunt</p>
  <p>Lorem ipsum dolor sit amet, consectetur adipiscing elit, sed do eiusmod tempor incididunt ut labore et dolore magna aliqua.Lorem ipsum dolor sit amet. Lorem ipsum dolor sit amet, consectetur adip iscing elit, sed do eiusmod tempor incididunt</p>
</div>
<div class="btn" style="left:636px;top:1305px;width:150px;height:50px;border-radius:3px">VIEW MORE</div>

<!-- services -->
<section class="services">
  <div class="eyebrow">What We Do</div>
  <h2>Services We Provide</h2>

  <div class="service" style="left:95px">
    <div class="photo" role="img" aria-label="Arborist pruning branches with long-handled loppers" style="background:linear-gradient(160deg,#6a9a3c,#2f4d22)"></div>
    <div class="badge"><b><svg width="30" height="30" viewBox="0 0 24 24" fill="none" stroke="#fff" stroke-width="1.6"><path d="M12 3l2.6 5.4 5.9.8-4.3 4.1 1 5.8L12 16.3 6.8 19.1l1-5.8L3.5 9.2l5.9-.8z"/></svg></b></div>
    <div class="caption"><h3>Tree Pruning</h3><div class="more">Read more <svg width="12" height="12" viewBox="0 0 24 24" fill="none" stroke="#555b66" stroke-width="2.2"><path d="M4 12h16M13 5l7 7-7 7"/></svg></div></div>
  </div>

  <div class="service" style="left:438px">
    <div class="photo" role="img" aria-label="Uprooted tree stump with roots on a lawn" style="background:linear-gradient(160deg,#9a8a5a,#4a5a2a)"></div>
    <div class="badge"><b><svg width="30" height="30" viewBox="0 0 24 24" fill="none" stroke="#fff" stroke-width="1.6"><path d="M6 20h12M9 20l3-9 3 9M12 11c-3 0-5-2-5-5 3 0 5 2 5 5zm0 0c0-3 2-5 5-5 0 3-2 5-5 5z"/></svg></b></div>
    <div class="caption"><h3>Tree Removal</h3><div class="more">Read more <svg width="12" height="12" viewBox="0 0 24 24" fill="none" stroke="#555b66" stroke-width="2.2"><path d="M4 12h16M13 5l7 7-7 7"/></svg></div></div>
  </div>

  <div class="service" style="left:781px">
    <div class="photo" role="img" aria-label="Two workers inspecting a hedge row in a garden" style="background:linear-gradient(160deg,#5e8a3a,#34522a)"></div>
    <div class="badge"><b><svg width="30" height="30" viewBox="0 0 24 24" fill="none" stroke="#fff" stroke-width="1.6"><circle cx="9" cy="8" r="3"/><circle cx="16" cy="9" r="2.5"/><path d="M3 19c0-3.3 2.7-5 6-5s6 1.7 6 5M14 14.2c3.3-.4 6 1.2 6 4.8"/></svg></b></div>
    <div class="caption"><h3>Stump Grinding</h3><div class="more">Read more <svg width="12" height="12" viewBox="0 0 24 24" fill="none" stroke="#555b66" stroke-width="2.2"><path d="M4 12h16M13 5l7 7-7 7"/></svg></div></div>
  </div>
</section>

<!-- why choose -->
<section class="why">
  <div class="label" style="left:115px;top:100px">Why Choose Us</div>
  <h2 class="section-title" style="left:114px;top:130px">Your Tree Care<br>Professionals</h2>
  <div class="tab active" style="left:105px;width:127px">Our Mission</div>
  <div class="tab" style="left:250px;width:115px">Our Vision</div>
  <div class="tab" style="left:380px;width:126px">Our History</div>
  <div class="abs" role="img" aria-label="Worker clearing fallen trees with a chainsaw" style="left:105px;top:325px;width:222px;height:229px;border-radius:6px;background:linear-gradient(160deg,#7d9aa8,#3e5a3a)"></div>
  <p class="intro">Lorem ipsum dolor sit amet, consectetur eiusmod tempor incididunt ut labore et do ipsum dolor sit amet. Lorem ipsum dolor si</p>
  <div class="check" style="top:444px"><svg width="15" height="15" viewBox="0 0 24 24" fill="none" stroke="#8cc63f" stroke-width="2.2"><rect x="3" y="3" width="18" height="18" rx="2"/><path d="M8 12l3 3 5-6"/></svg>Experts</div>
  <div class="check" style="top:478px"><svg width="15" height="15" viewBox="0 0 24 24" fill="none" stroke="#8cc63f" stroke-width="2.2"><rect x="3" y="3" width="18" height="18" rx="2"/><path d="M8 12l3 3 5-6"/></svg>Experienced</div>
  <div class="check" style="top:512px"><svg width="15" height="15" viewBox="0 0 24 24" fill="none" stroke="#8cc63f" stroke-width="2.2"><rect x="3" y="3" width="18" height="18" rx="2"/><path d="M8 12l3 3 5-6"/></svg>Professionalism</div>
  <div class="abs" role="img" aria-label="Two smiling workers in hard hats and safety vests holding plans" style="left:735px;top:65px;width:465px;height:557px;background:linear-gradient(180deg,#f3f4f3 0%,#d7dde4 25%,#b9c96a 70%,#6f7f8a 100%);border-radius:220px 220px 0 0"></div>
</section>

<!-- call to action -->
<section class="cta" role="img" aria-label="Blurred forest canopy in the background">
  <h2>Your Tree Care<br>Professionals</h2>
  <div class="btn">GET STARTED</div>
  <div class="pill" style="top:129px">We've expert and certified staff</div>
  <div class="pill" style="top:195px">We've expert and certified staff</div>
  <div class="pill" style="top:260px">We've expert and certified staff</div>
</section>

<!-- testimonials -->
<section class="reviews">
  <div class="label" style="width:100%;text-align:center;top:90px">Testimonials</div>
  <h2>Client Reviews</h2>

  <div class="review" style="left:93px">
    <div class="avatar" role="img" aria-label="Portrait of a client" style="background:linear-gradient(180deg,#e6e1da,#2a2f3a)"></div>
    <div class="who"><strong>Morgan Ellery</strong><small>CEO &amp; Founder</small></div>
    <div class="card">Lorem ipsum dolor sit amet, consect etur adipiscing elit, sed do eiusmod tempor incididunt ut labore et dolore magna aliqua.Lorem ipsum dolor sit amet.</div>
    <div class="quote">&#8220;</div>
  </div>
  <div class="review" style="left:439px">
    <div class="avatar" role="img" aria-label="Portrait of a client" style="background:linear-gradient(180deg,#e8e4dc,#b8a890)"></div>
    <div class="who"><strong>Morgan Ellery</strong><small>CEO &amp; Founder</small></div>
    <div class="card">Lorem ipsum dolor sit amet, consect etur adipiscing elit, sed do eiusmod tempor incididunt ut labore et dolore magna aliqua.Lorem ipsum dolor sit amet.</div>
    <div class="quote">&#8220;</div>
  </div>
  <div class="review" style="left:785px">
    <div class="avatar" role="img" aria-label="Portrait of a client" style="background:linear-gradient(180deg,#3a4656,#1e2633)"></div>
    <div class="who"><strong>Morgan Ellery</strong><small>CEO &amp; Founder</small></div>
    <div class="card">Lorem ipsum dolor sit amet, consect etur adipiscing elit, sed do eiusmod tempor incididunt ut labore et dolore magna aliqua.Lorem ipsum dolor sit amet.</div>
    <div class="quote">&#8220;</div>
  </div>

  <div class="btn" style="left:523px;top:567px;width:151px;height:48px;border-radius:3px">VIEW MORE</div>
</section>

<!-- footer -->
<footer class="footer">
  <svg class="abs" style="left:0;top:0" width="1200" height="519" viewBox="0 0 1200 519">
    <path d="M0 165 C 300 40 700 -5 1200 0 L1200 519 L0 519 Z" fill="#0b1428"/>
  </svg>
  <div class="abs" style="left:114px;top:206px;display:flex;align-items:center;gap:10px">
    <div style="width:44px;height:44px;background:#fff"></div>
    <div style="font-family:'Ubuntu',sans-serif;font-weight:700;font-size:24px;line-height:26px;color:#fff;width:150px">Quillby Tree Care</div>
  </div>
  <p style="left:114px;top:278px;width:280px;font-size:14px;line-height:24px">We have 14+ years experience Helping you overcome technology challenges</p>

  <div class="col-title" style="left:519px;top:197px">Newsletter</div>
  <p style="left:519px;top:250px;width:210px;font-size:11.5px;font-weight:700;line-height:24px">Subscribe to our newsletter to recieve updates or the latest news</p>
  <div class="abs" style="left:519px;top:333px;width:223px;height:41px;border-radius:4px;background:rgba(255,255,255,.22);display:flex;align-items:center;justify-content:space-between;padding:0 14px;color:#fff;font-size:12px;font-weight:600">Subscribe with us
    <svg width="18" height="18" viewBox="0 0 24 24" fill="none" stroke="#fff" stroke-width="2"><path d="M4 12h16M13 5l7 7-7 7"/></svg></div>

  <div class="col-title" style="left:862px;top:197px">Contacts</div>
  <svg class="abs" style="left:862px;top:252px" width="32" height="32" viewBox="0 0 24 24" fill="none" stroke="#8cc63f" stroke-width="1.4"><path d="M22 16.9v3a2 2 0 0 1-2.2 2 19.8 19.8 0 0 1-8.6-3.1 19.5 19.5 0 0 1-6-6A19.8 19.8 0 0 1 2.1 4.2 2 2 0 0 1 4.1 2h3a2 2 0 0 1 2 1.7c.1 1 .4 1.9.7 2.8a2 2 0 0 1-.5 2.1L8 9.9a16 16 0 0 0 6 6l1.3-1.3a2 2 0 0 1 2.1-.4c.9.3 1.8.6 2.8.7a2 2 0 0 1 1.7 2z"/></svg>
  <p style="left:910px;top:246px;font-family:'Ubuntu',sans-serif;font-weight:500;font-size:17px">Contact Us</p>
  <p style="left:910px;top:272px;font-size:13.5px">(44) 555-010-284</p>
  <svg class="abs" style="left:862px;top:330px" width="32" height="32" viewBox="0 0 24 24" fill="none" stroke="#8cc63f" stroke-width="1.4"><rect x="3" y="8" width="18" height="13" rx="1"/><path d="M3 9l9 6 9-6M7 8V3h10v5"/><circle cx="12" cy="7" r="1.8"/></svg>
  <p style="left:910px;top:325px;font-family:'Ubuntu',sans-serif;font-weight:500;font-size:17px">Mail Us</p>
  <p style="left:910px;top:350px;font-size:13.5px">hello@quillbytrees.com</p>

  <p style="left:0;width:1200px;text-align:center;top:484px;font-size:12px">Quillby Tree Care</p>
  <div class="abs" style="left:1066px;top:474px;width:33px;height:33px;background:#8cc63f;display:flex;align-items:center;justify-content:center"><svg width="14" height="14" viewBox="0 0 24 24" fill="none" stroke="#fff" stroke-width="2.2"><path d="M12 20V4M5 11l7-7 7 7"/></svg></div>
</footer>
<div class="social" style="left:114px"></div>
<div class="social" style="left:155px"></div>
<div class="social" style="left:196px"></div>
<div class="social" style="left:237px"></div>

</body>
</html>
```